Professional banners for an eyewear company

I have 3 images which need to be made into banners. Size 990 x 370, with a 10 pixel white border at top and bottom of banner.

They all need to be adjusted to make the colours better and less bright.
All will need some writing written on them with a nice serif font.

Banner 1 text: Handcrafted luxury eyewear, with a purpose...
Banner 2 text: Half of our profits go to help malnourished children in India
Banner 3 text: 10% of your first order, use code: First Order

On our homepage these 3 banners will alternate, so they need to look good together.

Tips
Please take a look at the banners on the lunvoreck.com homepage, this is kind of how I want the text to be displayed, and they use good colours.

The backgrounds on Banners 2 & 3 can be changed.
Banner 3 background if you can change to a nice colour, as per lunvoreck.com homepage.
Updates

Hi, just a quick update, thank you for all the designs submitted so far, please keep in mind that the brand is a luxury high-end brand so designs will need to reflect this.

Industry/Entity Type

Eyewear

```html
<!DOCTYPE html>
<html lang="en">
<head>
<meta charset="utf-8">
<title>Handcrafted luxury eyewear banner</title>
<link href="https://fonts.googleapis.com/css2?family=Cormorant+SC:wght@500;600&display=swap" rel="stylesheet">
<style>
  :root {
    --paper: #ffffff;
    --glow: #ffd24a;
    --amber: #f5a916;
    --orange: #ea8c0c;
    --deep-orange: #e0820a;
    --frame-shadow: #6b3a06;
    --ink-light: #fff6e6;
  }
  * { margin: 0; padding: 0; box-sizing: border-box; }
  html, body {
    width: 1200px;
    height: 473px;
    overflow: hidden;
    background: var(--paper);
  }
  .banner {
    position: absolute;
    left: 0;
    top: 13px;
    width: 1200px;
    height: 446px;
    overflow: hidden;
    background:
      radial-gradient(ellipse 420px 300px at 200px 130px, var(--glow) 0%, var(--amber) 45%, rgba(234,140,12,0) 100%),
      linear-gradient(90deg, var(--amber) 0%, var(--orange) 45%, var(--deep-orange) 100%);
  }
  .product-photo {
    position: absolute;
    left: 48px;
    top: 104px;
    width: 385px;
    height: 262px;
    border-radius: 40px;
    background:
      radial-gradient(ellipse 50% 40% at 45% 40%, rgba(107,58,6,0.45) 0%, rgba(107,58,6,0.15) 60%, rgba(107,58,6,0) 100%),
      radial-gradient(ellipse 50% 30% at 50% 82%, rgba(107,58,6,0.3) 0%, rgba(107,58,6,0) 100%);
  }
  .tagline {
    position: absolute;
    left: 490px;
    width: 700px;
    text-align: center;
    color: var(--ink-light);
    font-family: "Cormorant SC", "Times New Roman", serif;
    font-weight: 500;
  }
  .tagline-main {
    top: 170px;
    font-size: 37px;
    letter-spacing: 0.02em;
    white-space: nowrap;
  }
  .tagline-main .initial {
    font-size: 52px;
    line-height: 1;
  }
  .tagline-main .dot {
    font-size: 14px;
    vertical-align: 0.55em;
    margin: 0 10px;
  }
  .tagline-sub {
    top: 250px;
    font-size: 30px;
    letter-spacing: 0.12em;
  }
</style>
</head>
<body>
  <section class="banner">
    <div class="product-photo" role="img" aria-label="Photograph of black acetate glasses with amber lenses reflected on a glossy surface"></div>
    <h1 class="tagline tagline-main"><span class="dot">◆</span><span class="initial">H</span>andcrafted luxury eyewear<span class="dot">◆</span></h1>
    <p class="tagline tagline-sub">with a purpose...</p>
  </section>
</body>
</html>
```